IT Company needs a Wordpress Web Design

We need a wordpress website for a new IT Company called 'RQ Systems'. We develop educational software for Middle and High School Students and Staff. Our initial product is BrightDesk - a web app that allows School Counselors to track information about the students that they see. We would like to see modern designs that include the company logo and the BrightDesk logo

Target Market(s)

Educators

Industry/Entity Type

Information Technology

Coding

Coded - Design and coding required

Number of Pages Required

1 page

Font styles to use
Sans Serif

Requirements
Must have
• Must be able to use WordPress
Should not have
• No Flash

```html
<!DOCTYPE html>
<html lang="en">
<head>
<meta charset="utf-8">
<title>RQ Systems</title>
<link rel="stylesheet" href="https://fonts.googleapis.com/css2?family=Cinzel:wght@400;700&family=Lato:ital,wght@0,400;0,700;1,400&display=swap">
<style>
:root{
  --blue:#4a8bc9;
  --blue-dark:#2f6fae;
  --ink:#1b1b1b;
  --text:#2b2b2b;
  --red:#c0282d;
  --about-bg:#e6e6e6;
  --products-bg:#efefef;
  --news-bg:#e3e3e3;
  --footer-bg:#1f1f1f;
  --footer-bar:#161616;
  --white:#fff;
}
*{margin:0;padding:0;box-sizing:border-box}
html,body{width:719px;height:1200px;overflow:hidden}
body{position:relative;font-family:'Lato',sans-serif;color:var(--text);background:var(--white)}
.abs{position:absolute}

/* header */
.site-header{position:absolute;left:0;top:0;width:719px;height:66px;background:var(--white);border-top:2px solid var(--blue);border-bottom:1px solid #d6d6d6}
.brand{left:97px;top:16px;display:flex;align-items:center;gap:6px;font-weight:700;font-size:19px;color:var(--blue)}
.brand-mark{width:14px;height:14px;background:var(--blue)}
.top-contact{left:400px;top:-2px;height:23px;display:flex;font-size:9px;color:var(--white)}
.top-contact .phone{background:var(--blue);padding:6px 14px 0 24px;clip-path:polygon(12px 0,100% 0,100% 100%,0 100%)}
.top-contact .phone svg{vertical-align:-2px;margin-right:4px}
.top-contact .mail{background:var(--ink);padding:6px 18px 0 12px;clip-path:polygon(0 0,100% 0,calc(100% - 10px) 100%,0 100%)}
.main-nav{left:347px;top:36px;display:flex;font-family:'Cinzel',serif;font-size:11px;color:var(--ink)}
.main-nav span{padding:0 10px;border-left:1px solid #ccc;line-height:12px}
.main-nav span:first-child{border:0;padding-left:0;color:var(--blue)}

/* hero */
.hero{left:0;top:66px;width:719px;height:284px}
.hero-photo{position:absolute;inset:0;background:linear-gradient(90deg,#7fa8ab 0%,#2a2d31 10%,#1c1d20 45%,#6d9ea5 62%,#a9c9cb 100%)}
.slider-arrow{position:absolute;top:123px;width:26px;height:26px;border-radius:50%;border:1px solid rgba(255,255,255,.6);background:rgba(255,255,255,.15)}
.slider-arrow svg{position:absolute;left:7px;top:6px}
.hero-caption{position:absolute;left:345px;top:160px;width:374px;height:63px;background:rgba(20,20,20,.88);color:var(--white);font-weight:700;font-size:12px;line-height:16px;padding:16px 0 0 37px}
.dots{position:absolute;left:338px;top:268px;display:flex;gap:3px}
.dots i{width:8px;height:8px;border-radius:50%;border:1px solid #fff}
.dots i.on{background:#fff}

/* about */
.about{left:0;top:350px;width:719px;height:139px;background:var(--about-bg)}
.about h2{position:absolute;left:101px;top:51px;font-family:'Cinzel',serif;font-weight:400;font-size:25px;color:var(--ink)}
.about h2 em,.section-title em{font-style:normal;color:var(--blue)}
.about .divider{position:absolute;left:254px;top:23px;width:2px;height:94px;background:linear-gradient(var(--blue) 50%,var(--ink) 50%)}
.about p{position:absolute;left:284px;top:31px;width:340px;font-size:6.8px;line-height:13px}
.btn{display:inline-block;background:var(--blue);color:var(--white);font-size:7px;padding:2px 3px;border:1px solid var(--blue-dark)}
.about .btn{position:absolute;left:582px;top:103px}

/* products */
.products{left:0;top:489px;width:719px;height:293px;background:var(--products-bg)}
.section-title{font-family:'Cinzel',serif;font-weight:400;color:var(--ink)}
.products .section-title{position:absolute;left:280px;top:18px;font-size:21px;padding-bottom:2px;border-bottom:2px solid var(--ink)}
.products .underline{position:absolute;left:280px;top:42px;width:50px;height:2px;background:var(--blue)}
.product-brand{left:98px;top:88px;display:flex;align-items:center;gap:6px;font-weight:700;font-size:18px;color:var(--red)}
.product-brand .mark{width:12px;height:12px;background:var(--red)}
.product-sub{left:154px;top:108px;font-size:7px;color:var(--ink)}
.product-copy{left:98px;top:137px;width:166px;font-size:6.8px;line-height:10px}
.products .col1-btn{position:absolute;left:97px;top:257px}
.price{width:49px;height:49px;border-radius:50%;border:2px solid var(--red);background:var(--white);text-align:center;color:var(--ink)}
.price b{display:block;font-weight:400;font-size:15px;margin-top:7px;line-height:15px}
.price small{display:block;font-size:6.5px;line-height:7px}
.plan h3{font-family:'Cinzel',serif;font-weight:400;font-size:10px;color:var(--red);margin-bottom:4px}
.plan li{list-style:none;font-size:6px;line-height:12px;color:var(--ink)}
.plan li span{color:var(--blue);font-size:7.4px}
.round-arrow{width:20px;height:20px;border-radius:50%;background:#333}
.round-arrow svg{position:absolute;left:6px;top:5px}

/* news & testimonial */
.lower{left:0;top:782px;width:719px;height:238px;background:var(--news-bg)}
.lower .section-title{position:absolute;font-size:16px}
.rule{position:absolute;height:2px;background:var(--ink)}
.rule i{position:absolute;left:0;top:0;width:40px;height:2px;background:var(--blue)}
.mini-nav{position:absolute;display:flex;gap:2px}
.mini-nav i{width:8px;height:8px;border-radius:50%;border:1px solid #999}
.news-item{position:absolute;left:97px;width:240px}
.date{position:absolute;left:0;top:0;width:28px;text-align:center;color:var(--white)}
.date .d{display:block;background:var(--blue);font-family:'Cinzel',serif;font-size:13px;height:17px;line-height:17px}
.date .m{display:block;background:#2a2a2a;font-size:6px;height:13px;line-height:13px}
.news-item h4{margin-left:39px;font-size:7px;line-height:9px;font-weight:700;color:var(--ink);margin-bottom:3px}
.news-item p{margin-left:39px;font-size:7px;line-height:9.5px;color:var(--ink)}
.news-item a{display:block;margin-left:39px;margin-top:3px;font-size:6px;line-height:8px;color:var(--blue);font-weight:700;text-decoration:none}
.avatar{left:373px;top:70px;width:50px;height:50px;border-radius:50%;border:2px solid var(--blue);background:radial-gradient(circle at 50% 45%,#c9a48a 0 30%,#2b3440 31% 100%)}
.quote{left:436px;top:72px;width:188px;font-style:italic;font-size:7px;line-height:13px;color:#444}
.quote-name{left:373px;top:137px;font-size:7px;font-weight:700;color:var(--ink)}

/* footer */
.wave{left:0;top:940px}
.site-footer{left:0;top:1020px;width:719px;height:155px;background:var(--footer-bg);color:#cfcfcf}
.site-footer h5{font-family:'Cinzel',serif;font-weight:400;font-size:10px;color:var(--white);letter-spacing:.5px;padding-bottom:7px;border-bottom:1px solid #3a3a3a;white-space:nowrap}
.f-col{position:absolute;top:25px}
.links li{list-style:none;font-size:7.5px;line-height:15.5px}
.links li::before{content:"› ";color:#888}
.links li:first-child{color:var(--blue);margin-top:6px}
.contact-row{display:flex;gap:8px;font-size:7px;line-height:10px;margin-top:8px}
.contact-row.big{font-size:8.5px}
.news-copy{font-size:7px;line-height:10px;margin-top:8px}
.email-field{width:100px;height:15px;background:var(--white);margin-top:15px;color:#999;font-size:5.5px;padding:5px 9px}
.subscribe{display:inline-block;margin-top:10px;background:var(--blue);color:var(--white);font-size:7.5px;font-weight:700;padding:3px 6px}
.footer-brand{left:541px;top:44px;display:flex;align-items:center;gap:5px;font-weight:700;font-size:14px;color:var(--blue)}
.footer-brand .brand-mark{width:11px;height:11px}
.socials{left:541px;top:106px;display:flex;gap:6px}
.socials i{width:15px;height:15px;border-radius:50%;background:var(--blue)}
.copyright{left:0;top:1175px;width:719px;height:25px;background:var(--footer-bar);color:#ddd;font-size:7px;text-align:center;line-height:25px}
</style>
</head>
<body>

<header class="site-header">
  <div class="abs brand"><span class="brand-mark"></span>RQ Systems</div>
  <div class="abs top-contact">
    <div class="phone"><svg width="10" height="10" viewBox="0 0 10 10"><circle cx="5" cy="5" r="4.4" fill="none" stroke="#fff" stroke-width="0.8"/><path d="M3.3 2.6l1 1-.5.6c.3.6.8 1.1 1.4 1.4l.6-.5 1 1-.6.8C4.6 6.6 3.1 5.1 2.7 3.5z" fill="#fff"/></svg>+ 0 555-0142-778</div>
    <div class="mail">sales@rqsystems.com</div>
  </div>
  <nav class="abs main-nav"><span>Home</span><span>About</span><span>Our Products</span><span>Contact Us</span></nav>
</header>

<section class="abs hero">
  <div class="hero-photo" role="img" aria-label="Photo of a businessman in a dark suit holding a white tablet in an office"></div>
  <div class="slider-arrow" style="left:15px"><svg width="12" height="14"><path d="M8 1L2 7l6 6" fill="none" stroke="#fff" stroke-width="1.2"/></svg></div>
  <div class="slider-arrow" style="left:678px"><svg width="12" height="14"><path d="M3 1l6 6-6 6" fill="none" stroke="#fff" stroke-width="1.2"/></svg></div>
  <div class="hero-caption">We develop educational software for Middle<br>and High School Students and Staff.</div>
  <div class="dots"><i></i><i class="on"></i><i></i><i></i></div>
</section>

<section class="abs about">
  <h2>About <em>Us</em></h2>
  <div class="divider"></div>
  <p>Lorem ipsum dolor sit amet, consectetuer adipiscing elit, sed diam nonummy nibh euismod tincidunt ut laoreet dolore magna aliquam erat volutpat. Ut wisi enim ad minim veniam, quis nostrud exerci tation ullamcorper suscipit lobortis nisl ut aliquip ex ea commodo consequat. Duis autem vel eum iriure dolor consequat, vel illum dolore eu feugiat nulla facilisis at vero eros et accumsan et iusto odio dignissim qui blandit praesent luptatum zzril delenit augue duis dolore te feugait nulla facilisi. Exerci tation ullamcorper suscipit lobortis nisl ut aliquip ex ea commodo consequat...</p>
  <span class="btn">Read More</span>
</section>

<section class="abs products">
  <h2 class="section-title">Our <em>Products</em></h2>
  <div class="underline"></div>

  <div class="abs round-arrow" style="left:76px;top:136px"><svg width="8" height="10"><path d="M6 1L2 5l4 4" fill="none" stroke="#fff" stroke-width="1.4"/></svg></div>
  <div class="abs round-arrow" style="left:622px;top:136px"><svg width="8" height="10"><path d="M2 1l4 4-4 4" fill="none" stroke="#fff" stroke-width="1.4"/></svg></div>

  <div class="abs product-brand"><span class="mark"></span>BrightDesk</div>
  <div class="abs product-sub">The Electronic Sign In System</div>
  <p class="abs product-copy">Lorem ipsum dolor sit amet, consectetuer adipiscing elit, sed diam nonummy nibh euismod tincidunt ut laoreet dolore magna aliquam erat volutpat. Ut wisi enim ad minim veniam, quis nostrud exerci tation ullamcorper suscipit lobortis nisl ut aliquip ex ea commodo consequat. Duis autem vel eum iriure dolor in hendrerit in vulputate velit esse molestie consequat, vel illum dolore eu feugiat nulla facilisis at vero eros et accumsan et iusto odio dignissim qui blandit praesent luptatum zzril delenit augue duis dolore te feugait nulla facilisi.</p>
  <span class="btn col1-btn">Read More</span>

  <div class="abs price" style="left:343px;top:80px"><b>200 $</b><small>Per<br>School</small></div>
  <div class="abs plan" style="left:301px;top:138px">
    <h3>Coaching Packages</h3>
    <ul>
      <li><span>12 months</span> of access to BrightDesk</li>
      <li><span>Individual Accounts</span> for each School Counselor in</li>
      <li>your office</li>
      <li><span>Customizable</span> Student Login screen</li>
      <li>Access to a variety of <span>Data Reports</span> in Excel and</li>
      <li style="line-height:9px">PDF format</li>
      <li>Email <span>Product Support.</span></li>
    </ul>
  </div>

  <div class="abs price" style="left:528px;top:80px"><b>150 $</b><small>Per<br>School</small></div>
  <div class="abs plan" style="left:481px;top:138px">
    <h3>District Level Purchase</h3>
    <ul>
      <li><span>12 months</span> of access to BrightDesk for each school</li>
      <li><span>District level</span> access to information and reports</li>
      <li>District level <span>Account Controls</span></li>
      <li>Access to a variety of <span>Data Reports</span> in Excel and</li>
      <li style="line-height:9px">PDF format</li>
      <li>Email <span>Product Support.</span></li>
    </ul>
  </div>
</section>

<section class="abs lower">
  <h2 class="section-title" style="left:98px;top:20px">Latest <em>News</em></h2>
  <div class="mini-nav" style="left:320px;top:32px"><i></i><i style="border-color:#555"></i></div>
  <div class="rule" style="left:98px;top:44px;width:243px"><i></i></div>

  <article class="news-item" style="top:58px">
    <div class="date"><span class="d">03</span><span class="m">FEB</span></div>
    <h4>Duis autem vel eum iriure dolor in hendrerit molestie</h4>
    <p>Lorem ipsum dolor sit amet, consectetuer adipiscing elit, sed diam nonummy nibh euismod tincidunt ut laoreet</p>
    <a>Read More »</a>
  </article>
  <div class="abs" style="left:136px;top:108px;width:195px;height:1px;background:#cfcfcf"></div>
  <article class="news-item" style="top:120px">
    <div class="date"><span class="d">01</span><span class="m">FEB</span></div>
    <h4>Allamcorper suscipit lobortis col hendrerit in vulputate</h4>
    <p>Lorem ipsum dolor sit amet, consectetuer adipiscing elit, sed diam nonummy nibh euismod tinci</p>
    <a>Read More »</a>
  </article>

  <h2 class="section-title" style="left:376px;top:24px">Client <em>Testimonial</em></h2>
  <div class="mini-nav" style="left:602px;top:32px"><i></i><i style="border-color:#555"></i></div>
  <div class="rule" style="left:376px;top:47px;width:246px"><i></i></div>
  <div class="abs avatar" role="img" aria-label="Portrait photo of the client"></div>
  <p class="abs quote">“ Lorem ipsumn sit amet co adipisclitsedudml eiusmo dtepor incididunt ut la dolore ma aliquanmi kni enim nim veni exercitation ullamco ips sdlitnol ameti co adipiscig elitsed do eiusmod te epo uom Accusant dol oremque laudantium. ”</p>
  <div class="abs quote-name">- Marlo Kent</div>
</section>

<svg class="abs wave" width="719" height="82" viewBox="0 0 719 82">
  <path d="M0 4 C110 60 250 88 719 18 L719 82 L0 82 Z" fill="#4a8bc9"/>
  <path d="M0 40 C140 86 330 84 719 12 L719 82 L0 82 Z" fill="#1f1f1f"/>
</svg>

<footer class="abs site-footer">
  <div class="f-col" style="left:96px;width:107px">
    <h5>Quick Links</h5>
    <ul class="links"><li>Home</li><li>About Us</li><li>Our Products</li><li>Contact Us</li></ul>
  </div>
  <div class="f-col" style="left:231px;width:134px">
    <h5>Contact Information</h5>
    <div class="contact-row"><svg width="6" height="9" viewBox="0 0 6 9"><path d="M3 0a3 3 0 0 1 3 3c0 2-3 6-3 6S0 5 0 3a3 3 0 0 1 3-3z" fill="#ccc"/><circle cx="3" cy="3" r="1.1" fill="#1f1f1f"/></svg><span>123 Lorem-ipsum,<br>Lorem-ipsum, Lorem-ipsum<br>987654</span></div>
    <div class="contact-row big"><svg width="7" height="8" viewBox="0 0 7 8"><path d="M1 0l2 2-1 1c.5 1 1.2 1.8 2 2.2l1-1 2 2-1 1.6C3.3 7.5.3 4.3 0 1z" fill="#ccc"/></svg><span>(555) 019 - 4821</span></div>
    <div class="contact-row" style="margin-top:12px"><svg width="8" height="6" viewBox="0 0 8 6"><rect width="8" height="6" fill="#ccc"/><path d="M0 0l4 3 4-3" fill="none" stroke="#1f1f1f" stroke-width=".8"/></svg><span>sales@rqsystems.com</span></div>
  </div>
  <div class="f-col" style="left:403px;width:118px">
    <h5>Newsletter Sign Up</h5>
    <p class="news-copy">Lorem ipsum dolor sit amet,<br>consectetuer adipiscing elit,</p>
    <div class="email-field">Email Address</div>
    <span class="subscribe">Subscribe</span>
  </div>
  <div class="abs footer-brand"><span class="brand-mark"></span>RQ Systems</div>
  <div class="abs socials"><i></i><i></i><i></i><i></i></div>
</footer>

<div class="abs copyright">Copyright 2017 RQSYSTEMS.COM. All rights reserved.</div>

</body>
</html>
```